Kaffeerösterei sucht Etiketten-Design
- schnelle Ausführung - mein Geschmack voll getroffen - unkompliziert und Kunden orientiert bei der Ausführung
Zielgruppe
Kaffeerösterei für die edelsten und teuersten Rohkaffees.
Meine Kunden sind Kaffee Geniesser.
Aufgabenstellung
Transparente Aufkleber für eine Schiefertafel im Format 22.5 cm x 15.5 cm.
Im Hand-Lettering Stil.
5 Schiefertafeln sind gewünscht.
Tafel 1
Kostenlos zur Degustation
Espresso
Café Crème 3.--
Americano 3.--
Filter Kaffee 3.--
Tafel 2
Kaffee & Milch
Cappuccino 4.--
Café Latte 4.--
Flat White 4.--
Latte Macchiato 4.--
Latte Macchiato mit Aroma 5.--
Kaffee & Hafermilch + 1.--
Tafel 3
Crepes
Pikant
- Pizza Crepes 7.--
- Flammkuchen Crepes 7.--
Süss
- Schoggi Crepes 6.--
- Apfelmus & Zimtzucker 6.--
Tafel 4
Kaffee & Schnaps
- Original Entlebucher Schwarzes 7.--
- Espresso Coretto 5.00
- Schwarzes mit Rahmhaube 8.--
Tafel 5
Schokolade & Milch
- heisse Schoggi 5.--
- heisse Schoggi mit Rahmhaube 6.--
- heisse Schoggi mit Espresso 6.--
- Schokolade & Hafermilch +1.--
Als Idee, was mir gefallen könnte:
https://www.bildsammlung.example/pin/551203948817265034/
https://de.grafikquelle.example/vektorkunst/4182093-set-kaffeekarte-mit-tassen-kaffeegetranken-im-vintage-stil-stilisierte-zeichnung-mit-kreide-auf-tafel-schriftzug-know-your-coffee
https://www.fotoarchiv.example/stockfoto-heisser-kakao-bar-warm-hier-oben-hand-tafel-caf-schild-an-tafel-hintergrund-mit-farbe-kreide-schriftzug-werbung-fur-heisse-d-837215406.html

```html
<!DOCTYPE html>
<html lang="de">
<head>
<meta charset="utf-8">
<title>Tafel 1 – Kostenlos zur Degustation</title>
<link rel="stylesheet" href="https://fonts.googleapis.com/css2?family=Amatic+SC:wght@700&display=swap">
<style>
  :root {
    --paper: #ffffff;
    --slate: #1d1d1b;
    --chalk: #ffffff;
    --gold: #fdd17a;
    --cream: #fbe7cf;
    --chalk-haze: #d8d8d3;
    --chalk-mist: #6d6d69;
  }
  html, body {
    margin: 0;
    padding: 0;
    width: 1200px;
    height: 864px;
    overflow: hidden;
    background: var(--paper);
  }
  .board {
    display: block;
    width: 1200px;
    height: 864px;
  }
  .lettering {
    font-family: "Amatic SC", cursive;
    font-weight: 700;
    paint-order: stroke fill;
    stroke-linejoin: round;
  }
  .headline { fill: var(--gold); stroke: var(--gold); stroke-width: 2.4; }
  .title { fill: var(--chalk); stroke: var(--chalk); stroke-width: 2.6; }
  .item { fill: var(--chalk); stroke: var(--chalk); stroke-width: 2.6; }
  .price { fill: var(--cream); stroke: var(--cream); stroke-width: 3.2; }
  .slate { fill: var(--slate); }
  .chalk-line {
    fill: none;
    stroke: var(--chalk);
    stroke-width: 3.5;
    stroke-linecap: round;
  }
  .gold-stroke {
    fill: none;
    stroke: var(--gold);
    stroke-linecap: round;
  }
  .chalk-dot { fill: var(--chalk); }
</style>
</head>
<body>
<svg class="board" viewBox="0 0 1200 864" xmlns="http://www.w3.org/2000/svg">
  <defs>
    <radialGradient id="brewer-tone" cx="0.5" cy="0.55" r="0.6">
      <stop offset="0" stop-color="var(--chalk-haze)" stop-opacity="0.85"/>
      <stop offset="0.55" stop-color="var(--chalk-mist)" stop-opacity="0.6"/>
      <stop offset="1" stop-color="var(--slate)" stop-opacity="0"/>
    </radialGradient>
  </defs>

  <!-- slate board -->
  <rect class="slate" x="61" y="60" width="1076" height="741"/>

  <!-- chalk frame -->
  <g class="frame">
    <path class="chalk-line" d="M86 89 L398 82"/>
    <path class="chalk-line" d="M412 83 L424 83 M435 83 L440 83 M459 84 L466 85"/>
    <path class="chalk-line" d="M773 86 L779 87 M795 87 L808 87"/>
    <path class="chalk-line" d="M818 87 L1106 94"/>
    <path class="chalk-line" d="M86 89 L88 772"/>
    <path class="chalk-line" d="M1106 94 L1108 770"/>
    <path class="chalk-line" d="M88 772 L1108 766"/>
    <path class="chalk-line" d="M109 700 L112 746"/>
    <path class="chalk-line" d="M123 750 L165 746"/>
    <path class="chalk-line" d="M1084 717 L1087 742"/>
    <path class="chalk-line" d="M1046 744 L1078 747"/>
    <circle class="chalk-dot" cx="110" cy="680" r="3"/>
    <circle class="chalk-dot" cx="186" cy="748" r="3"/>
    <circle class="chalk-dot" cx="1085" cy="690" r="3"/>
    <circle class="chalk-dot" cx="1030" cy="746" r="3"/>
  </g>

  <!-- headline -->
  <text class="lettering headline" x="600" y="183" text-anchor="middle"
        font-size="80" textLength="754" lengthAdjust="spacingAndGlyphs">Kostenlos zur Degustation</text>

  <!-- title with gold rays -->
  <g class="title-group">
    <path class="gold-stroke" stroke-width="7" d="M337 239 Q356 240 383 247"/>
    <path class="gold-stroke" stroke-width="7" d="M319 270 Q345 268 375 265"/>
    <path class="gold-stroke" stroke-width="7" d="M349 296 Q365 288 382 274"/>
    <path class="gold-stroke" stroke-width="7" d="M862 239 Q843 240 816 247"/>
    <path class="gold-stroke" stroke-width="7" d="M878 270 Q852 268 824 265"/>
    <path class="gold-stroke" stroke-width="7" d="M850 296 Q834 288 817 274"/>
    <text class="lettering title" x="599" y="306" text-anchor="middle"
          font-size="112" textLength="346" lengthAdjust="spacingAndGlyphs">ESPRESSO</text>
  </g>

  <!-- brewer illustration area -->
  <rect class="illustration" role="img"
        aria-label="Kreidezeichnung einer Kaffeepresse, die auf einer Tasse steht"
        x="126" y="255" width="208" height="437" rx="60" fill="url(#brewer-tone)"/>

  <!-- menu -->
  <g class="menu">
    <text class="lettering item" x="762" y="447" text-anchor="end"
          font-size="76" textLength="310" lengthAdjust="spacingAndGlyphs">Café Crème</text>
    <text class="lettering price" x="907" y="447" text-anchor="end"
          font-size="76" textLength="113" lengthAdjust="spacingAndGlyphs">3,–</text>

    <text class="lettering item" x="762" y="535" text-anchor="end"
          font-size="76" textLength="294" lengthAdjust="spacingAndGlyphs">Americano</text>
    <text class="lettering price" x="907" y="535" text-anchor="end"
          font-size="76" textLength="113" lengthAdjust="spacingAndGlyphs">3,–</text>

    <text class="lettering item" x="762" y="624" text-anchor="end"
          font-size="76" textLength="372" lengthAdjust="spacingAndGlyphs">Filter Kaffee</text>
    <text class="lettering price" x="907" y="624" text-anchor="end"
          font-size="76" textLength="113" lengthAdjust="spacingAndGlyphs">3,–</text>
  </g>

  <!-- gold underline -->
  <path class="gold-stroke" stroke-width="9" d="M355 688 Q500 678 620 679 Q760 680 832 693"/>
</svg>
</body>
</html>
```